Velmora Biz Card 2019

New business card for Velmora Property Inspections. We are a residential home inspection company in Arizona.

Target Market(s)

Real Estate

Font styles to use
Sans Serif

Requirements
Must have
• Glen Mirewick
• Home Inspector
• Velmora Property Inspections, LLC
• 480-555-0172
• glen@velmora-llc.example

```html
<!DOCTYPE html>
<html lang="en">
<head>
<meta charset="utf-8">
<title>Velmora Biz Card 2019</title>
<link rel="stylesheet" href="https://fonts.googleapis.com/css2?family=Montserrat:wght@400;600;700&display=swap">
<style>
  :root {
    --stage: #2b2e31;
    --card: #1e1e1f;
    --accent: #3fb83a;
    --ink: #f2f2f2;
    --ink-soft: #d6d6d6;
  }
  html, body {
    margin: 0;
    padding: 0;
    width: 1200px;
    height: 900px;
    overflow: hidden;
    background: var(--stage);
    font-family: "Montserrat", sans-serif;
  }
  .business-card {
    position: absolute;
    left: 100px;
    top: 164px;
    width: 1000px;
    height: 572px;
    background: var(--card);
    box-shadow: 0 14px 40px rgba(0,0,0,0.45);
  }
  .card-frame {
    position: absolute;
    inset: 24px;
    border: 3px solid var(--accent);
  }
  .brand {
    position: absolute;
    left: 64px;
    top: 58px;
    display: flex;
    align-items: center;
    gap: 12px;
  }
  .brand-mark {
    width: 18px;
    height: 18px;
    background: var(--accent);
  }
  .brand-name {
    color: var(--ink);
    font-weight: 700;
    font-size: 26px;
    letter-spacing: 1px;
    text-transform: uppercase;
  }
  .identity {
    position: absolute;
    right: 80px;
    top: 150px;
    text-align: right;
  }
  .company-name {
    color: var(--ink);
    font-weight: 600;
    font-size: 15px;
    letter-spacing: 2.4px;
    margin: 0 0 40px;
  }
  .person-name {
    color: var(--ink);
    font-weight: 700;
    font-size: 34px;
    letter-spacing: 1px;
    margin: 0;
  }
  .person-title {
    color: var(--accent);
    font-weight: 400;
    font-size: 19px;
    letter-spacing: 1px;
    margin: 6px 0 0;
  }
  .contact {
    position: absolute;
    right: 250px;
    top: 370px;
    text-align: right;
    color: var(--ink-soft);
    font-size: 19px;
    line-height: 1.55;
    letter-spacing: 0.8px;
    font-style: normal;
  }
  .contact span { display: block; }
</style>
</head>
<body>
  <div class="business-card">
    <div class="card-frame"></div>

    <div class="brand">
      <span class="brand-mark"></span>
      <span class="brand-name">Velmora</span>
    </div>

    <div class="identity">
      <p class="company-name">Velmora Property Inspections, LLC</p>
      <p class="person-name">Glen Mirewick</p>
      <p class="person-title">Home Inspector</p>
    </div>

    <address class="contact">
      <span>4410 S. Harlow Ave.</span>
      <span>Larkfield, AZ 85000</span>
      <span>480-555-0172</span>
      <span>glen@velmora-llc.example</span>
    </address>
  </div>
</body>
</html>
```